Music Artist Needs Flyer Design ASAP

Looking for a flyer design to promote for artist release party. Music artist is mainly hip hop based. We would like designs that are simple, creative and eye catching.

Requirements
Must have
• The flyer must have the photo of the artist I attached incorporated into the design. Must say "Free ZUKO" Release Party, Live at Tolly's Bar Thursday Dec.27 2012 (artist name=ZUKO VeN), show starts at 8pm, No cover charge, 21 and over, Register to Win Coral Blaze tickets Giveaway

```html
<!DOCTYPE html>
<html lang="en">
<head>
<meta charset="utf-8">
<title>Free ZUKO Release Party – Tolly's Bar</title>
<link rel="stylesheet" href="https://fonts.googleapis.com/css2?family=Poppins:wght@300;400;600;700;800&family=Questrial&display=swap">
<style>
  :root {
    --ink-white: #ffffff;
    --venue-purple: #3a2a86;
    --day-blue: #3e4f9e;
    --date-blue: #2f6aa6;
    --time-teal: #63bdb3;
    --artist-gold: #d99f2b;
    --prize-pale: #cbe4ec;
    --prize-teal: #5ec6c4;
    --handle-blue: #5a5fb2;
    --night: #050a0c;
  }
  * { margin: 0; padding: 0; box-sizing: border-box; }
  html, body { width: 1200px; height: 848px; overflow: hidden; background: var(--night); }
  .flyer {
    position: relative; width: 1200px; height: 848px; overflow: hidden;
    font-family: "Poppins", "Questrial", sans-serif; color: var(--ink-white);
  }
  .artist-photo {
    position: absolute; inset: 0;
    background:
      radial-gradient(ellipse 260px 340px at 500px 380px, #d8a23a 0%, rgba(216,162,58,0) 70%),
      radial-gradient(ellipse 380px 420px at 140px 300px, #c2361c 0%, rgba(194,54,28,0) 75%),
      radial-gradient(ellipse 420px 360px at 900px 380px, #a98a3c 0%, rgba(169,138,60,0) 75%),
      linear-gradient(135deg, #8a2a14 0%, #c9681f 35%, #6d5a2c 60%, #3b3a2c 100%);
  }
  .night-band {
    position: absolute; left: 0; right: 0; top: 500px; bottom: 0;
    background: linear-gradient(to bottom, rgba(5,10,12,0) 0%, rgba(5,10,12,.75) 28%, #071214 55%, var(--night) 100%);
  }
  .venue-block { position: absolute; right: 52px; top: 14px; text-align: center; width: 470px; }
  .live-at { font-family: "Questrial", sans-serif; font-size: 86px; line-height: 1; letter-spacing: -3px; margin-left: 40px; text-shadow: 0 2px 4px rgba(0,0,0,.4); }
  .venue-name { font-weight: 800; font-size: 98px; line-height: .95; letter-spacing: -4px; color: var(--venue-purple); text-shadow: 0 3px 3px rgba(0,0,0,.35); }
  .show-day { font-weight: 800; font-size: 58px; line-height: 1; letter-spacing: -3px; color: var(--day-blue); margin-left: 14px; }
  .show-date { font-weight: 700; font-size: 80px; line-height: .95; letter-spacing: -3px; color: var(--date-blue); text-shadow: 0 3px 3px rgba(0,0,0,.35); }
  .show-time { font-weight: 600; font-size: 42px; line-height: 1.1; letter-spacing: -2px; color: var(--time-teal); }
  .entry-notes { position: absolute; right: 33px; top: 515px; font-family: "Questrial", sans-serif; font-size: 21px; }
  .party-title {
    position: absolute; left: 26px; top: 535px; width: 1150px;
    font-weight: 800; font-size: 91px; letter-spacing: -4px; line-height: 1.1; white-space: nowrap;
    text-shadow: 0 0 14px rgba(255,255,255,.35);
  }
  .featuring { position: absolute; left: 186px; top: 645px; white-space: nowrap; display: flex; align-items: baseline; gap: 18px; }
  .featuring-label { font-family: "Questrial", sans-serif; font-size: 46px; }
  .artist-name { font-family: "Questrial", sans-serif; font-size: 84px; color: var(--artist-gold); letter-spacing: 2px; font-weight: 700; -webkit-text-stroke: 2px var(--artist-gold); }
  .giveaway { position: absolute; left: 28px; top: 728px; font-weight: 600; font-size: 51px; letter-spacing: -2px; white-space: nowrap; color: var(--prize-pale); }
  .giveaway .prize { color: var(--prize-teal); }
  .contact { position: absolute; left: 30px; top: 806px; font-family: "Questrial", sans-serif; font-size: 21px; white-space: nowrap; }
  .contact strong { font-family: "Poppins", sans-serif; font-weight: 700; font-size: 24px; }
  .fan-page { position: absolute; right: 28px; top: 800px; font-weight: 600; font-size: 29px; letter-spacing: -.5px; color: var(--handle-blue); }
</style>
</head>
<body>
<main class="flyer">
  <div class="artist-photo" role="img" aria-label="Photo of the artist in a white T-shirt and chain in front of a graffiti-covered wall"></div>
  <div class="night-band"></div>

  <section class="venue-block">
    <p class="live-at">Live at</p>
    <h2 class="venue-name">TOLLYS BAR</h2>
    <p class="show-day">THURSDAY</p>
    <p class="show-date">DEC. 27/2012</p>
    <p class="show-time">show starts at 8pm*</p>
  </section>

  <p class="entry-notes">✱ No cover charge &nbsp;✱ 21 and over</p>

  <h1 class="party-title">FREE ZUKO RELEASE PARTY</h1>

  <p class="featuring"><span class="featuring-label">FEATURING :</span><span class="artist-name">ZUKO VeN</span></p>

  <p class="giveaway">Register to Win <span class="prize">Coral Blaze tickets</span> Giveaway</p>

  <p class="contact">CONTACT &amp; BOOKING <strong>+198765432 // bookings@zukoven.example</strong></p>
  <p class="fan-page">zukoven.example/live</p>
</main>
</body>
</html>
```